Real State Agency App

We need an app design for a real state agency, we provide mockups for our project that ilustrates very well what we need
our web site is www.brightkeyhomes-example.com,

Target Market(s)

Tourism

Font styles to use
Other font styles liked:
• attached you will find it

Requirements
Must have
• Colors like the logo

```html
<!DOCTYPE html>
<html lang="en">
<head>
<meta charset="utf-8">
<title>Contact Us</title>
<link href="https://fonts.googleapis.com/css2?family=Montserrat:wght@300;400;500;600;700&display=swap" rel="stylesheet">
<style>
  :root {
    --brand-deep: #0a98d5;
    --brand-bright: #06c8e8;
    --brand-teal: #0bc6cf;
    --accent: #1a9bd7;
    --page-bg: #eef2f4;
    --field-bg: #ffffff;
    --divider: #dde3e7;
    --placeholder: #8a8f94;
    --tab-text: #777c80;
    --white: #ffffff;
  }
  * { box-sizing: border-box; margin: 0; padding: 0; }
  html, body { width: 1200px; height: 2349px; overflow: hidden; background: var(--page-bg); }
  body { font-family: "Montserrat", Arial, sans-serif; }
  .screen {
    position: absolute; left: 0; top: 0;
    width: 375px; height: 734px;
    transform: scale(3.2); transform-origin: 0 0;
    background: var(--page-bg);
    overflow: hidden;
  }
  .hero {
    position: absolute; left: 0; top: 0; width: 375px; height: 200px;
    background: linear-gradient(110deg, var(--brand-deep) 0%, var(--brand-bright) 100%);
    color: var(--white);
  }
  .status-bar {
    position: absolute; top: 0; left: 0; width: 100%; height: 20px;
    font-size: 12px; font-weight: 500; color: var(--white);
  }
  .status-bar .carrier { position: absolute; left: 6px; top: 3px; display: flex; align-items: center; gap: 4px; }
  .status-bar .time { position: absolute; left: 0; right: 0; top: 3px; text-align: center; font-weight: 600; }
  .status-bar .battery { position: absolute; right: 6px; top: 3px; display: flex; align-items: center; gap: 4px; }
  .hero-title { position: absolute; top: 32px; width: 100%; text-align: center; font-size: 15px; font-weight: 600; }
  .hero-icon { position: absolute; top: 80px; left: 161px; }
  .hero-question { position: absolute; top: 128px; width: 100%; text-align: center; font-size: 21px; font-weight: 400; letter-spacing: 0.2px; }

  .field-group { position: absolute; left: 0; width: 375px; background: var(--field-bg); border-top: 1px solid var(--divider); border-bottom: 1px solid var(--divider); }
  .field { position: relative; height: 51px; display: flex; align-items: center; padding-left: 16px; border-bottom: 1px solid var(--divider); }
  .field:last-child { border-bottom: none; }
  .field svg { flex: none; }
  .field-label { margin-left: 8px; font-size: 14px; color: var(--placeholder); }
  .contact-fields { top: 208px; }
  .property-field { top: 420px; }
  .property-field .chevron { position: absolute; right: 10px; top: 17px; }
  .notes-field { top: 479px; height: 133px; }
  .notes-field .field { align-items: flex-start; padding-top: 17px; height: 131px; border-bottom: none; }

  .send-button {
    position: absolute; left: 7px; top: 621px; width: 361px; height: 55px;
    border-radius: 4px; border: none;
    background: linear-gradient(90deg, var(--brand-deep) 0%, var(--brand-teal) 100%);
    color: var(--white); font-family: "Montserrat", Arial, sans-serif;
    font-size: 14px; font-weight: 700;
    display: flex; align-items: center; justify-content: center; gap: 10px;
  }

  .tab-bar {
    position: absolute; left: 0; top: 686px; width: 375px; height: 48px;
    background: var(--white); border-top: 1px solid var(--divider);
    display: flex;
  }
  .tab { flex: 1; display: flex; flex-direction: column; align-items: center; padding-top: 6px; font-size: 11px; color: var(--tab-text); }
  .tab svg { margin-bottom: 2px; }
  .tab.is-active { color: var(--accent); font-weight: 700; }
</style>
</head>
<body>
<div class="screen">
  <header class="hero">
    <div class="status-bar">
      <div class="carrier">
        <svg width="18" height="10" viewBox="0 0 18 10"><rect x="0" y="7" width="3" height="3" fill="#fff"/><rect x="4" y="5" width="3" height="5" fill="#fff"/><rect x="8" y="3" width="3" height="7" fill="#fff"/><rect x="12" y="0" width="3" height="10" fill="#fff"/></svg>
        <span>Carrier</span>
        <svg width="14" height="10" viewBox="0 0 14 10"><path d="M1 3.5a9 9 0 0 1 12 0M3 5.8a6 6 0 0 1 8 0M5 8a3 3 0 0 1 4 0" stroke="#fff" stroke-width="1.5" fill="none" stroke-linecap="round"/></svg>
      </div>
      <div class="time">9:41 AM</div>
      <div class="battery">
        <svg width="7" height="11" viewBox="0 0 7 11"><path d="M1 3l5 5-2.5 2.5V0.5L6 3 1 8" stroke="#fff" stroke-width="1.1" fill="none"/></svg>
        <span>100%</span>
        <svg width="24" height="11" viewBox="0 0 24 11"><rect x="0.5" y="0.5" width="21" height="10" rx="2" stroke="#fff" fill="none"/><rect x="2" y="2" width="18" height="7" rx="1" fill="#fff"/><rect x="22.5" y="3.5" width="1.5" height="4" fill="#fff"/></svg>
      </div>
    </div>
    <h1 class="hero-title">Contact Us</h1>
    <svg class="hero-icon" width="52" height="44" viewBox="0 0 52 44">
      <path d="M3 3h30v20H15l-7 6v-6H3z" stroke="#fff" stroke-width="2.6" fill="none" stroke-linejoin="round"/>
      <path d="M33 13h15v20h-5v6l-7-6H19v-10" stroke="#fff" stroke-width="2.6" fill="none" stroke-linejoin="round"/>
    </svg>
    <p class="hero-question">Got a question?</p>
  </header>

  <div class="field-group contact-fields">
    <div class="field">
      <svg width="14" height="15" viewBox="0 0 14 15"><circle cx="7" cy="4.5" r="3.5" stroke="#1a9bd7" stroke-width="1.4" fill="none"/><path d="M1 14c0-4 2.7-5.5 6-5.5s6 1.5 6 5.5" stroke="#1a9bd7" stroke-width="1.4" fill="none"/></svg>
      <span class="field-label">First name</span>
    </div>
    <div class="field">
      <svg width="14" height="15" viewBox="0 0 14 15"><circle cx="7" cy="4.5" r="3.5" stroke="#1a9bd7" stroke-width="1.4" fill="none"/><path d="M1 14c0-4 2.7-5.5 6-5.5s6 1.5 6 5.5" stroke="#1a9bd7" stroke-width="1.4" fill="none"/></svg>
      <span class="field-label">Surname</span>
    </div>
    <div class="field">
      <svg width="16" height="16" viewBox="0 0 16 16"><path d="M3 1.5l3 3-1.7 2a9 9 0 0 0 5 5l2-1.7 3 3-1.8 1.8C8 15 1 8 1.2 3.3z" stroke="#1a9bd7" stroke-width="1.3" fill="none" stroke-linejoin="round"/></svg>
      <span class="field-label">Phone</span>
    </div>
    <div class="field">
      <svg width="17" height="12" viewBox="0 0 17 12"><rect x="0.7" y="0.7" width="15.6" height="10.6" stroke="#1a9bd7" stroke-width="1.3" fill="none"/><path d="M1 1l7.5 6L16 1" stroke="#1a9bd7" stroke-width="1.3" fill="none"/></svg>
      <span class="field-label">Email</span>
    </div>
  </div>

  <div class="field-group property-field">
    <div class="field">
      <svg width="16" height="16" viewBox="0 0 16 16"><path d="M1 6L8 1l7 5" stroke="#1a9bd7" stroke-width="1.3" fill="none"/><rect x="2.5" y="5.5" width="11" height="9.5" stroke="#1a9bd7" stroke-width="1.3" fill="none"/><rect x="4.5" y="8" width="3" height="3" stroke="#1a9bd7" stroke-width="1.1" fill="none"/><path d="M9.5 15V9h2.5v6" stroke="#1a9bd7" stroke-width="1.1" fill="none"/></svg>
      <span class="field-label">Property</span>
      <svg class="chevron" width="16" height="10" viewBox="0 0 16 10"><path d="M1 1.5l7 7 7-7" stroke="#9aa0a5" stroke-width="1.5" fill="none"/></svg>
    </div>
  </div>

  <div class="field-group notes-field">
    <div class="field">
      <svg width="16" height="16" viewBox="0 0 16 16"><path d="M11.5 1.5l3 3L5 14l-4 1 1-4z M9.5 3.5l3 3" stroke="#1a9bd7" stroke-width="1.3" fill="none" stroke-linejoin="round"/></svg>
      <span class="field-label">Notes</span>
    </div>
  </div>

  <button class="send-button">
    <svg width="16" height="16" viewBox="0 0 16 16"><path d="M15.5 0.5L0.5 7l6 2.5 2.5 6z" fill="#fff"/><path d="M6.5 9.5L15.5 0.5" stroke="#0aa0d6" stroke-width="1"/></svg>
    <span>Send</span>
  </button>

  <nav class="tab-bar">
    <div class="tab">
      <svg width="18" height="18" viewBox="0 0 18 18"><circle cx="10.5" cy="7" r="5.5" stroke="#777c80" stroke-width="1.3" fill="none"/><path d="M6.5 11L1.5 16" stroke="#777c80" stroke-width="1.5"/></svg>
      <span>Search</span>
    </div>
    <div class="tab">
      <svg width="18" height="18" viewBox="0 0 18 18"><path d="M9.5 1.5H16.5V8.5L8.5 16.5 1.5 9.5z" stroke="#777c80" stroke-width="1.3" fill="none" stroke-linejoin="round"/><circle cx="13" cy="5" r="1.2" fill="#777c80"/></svg>
      <span>Sell</span>
    </div>
    <div class="tab">
      <svg width="18" height="18" viewBox="0 0 18 18"><circle cx="9" cy="9" r="2.6" stroke="#777c80" stroke-width="1.3" fill="none"/><path d="M7.6 1.5h2.8l.4 2.1 1.5.9 2-.8 1.4 2.4-1.6 1.4v1.7l1.6 1.4-1.4 2.4-2-.8-1.5.9-.4 2.1H7.6l-.4-2.1-1.5-.9-2 .8-1.4-2.4 1.6-1.4V8.1L2.3 6.7l1.4-2.4 2 .8 1.5-.9z" stroke="#777c80" stroke-width="1.2" fill="none" stroke-linejoin="round"/></svg>
      <span>Our Services</span>
    </div>
    <div class="tab is-active">
      <svg width="18" height="18" viewBox="0 0 18 18"><path d="M1.5 2h15v10.5H10L7 15.5v-3H1.5z" stroke="#1a9bd7" stroke-width="1.4" fill="none" stroke-linejoin="round"/><circle cx="5.5" cy="7.3" r="1" fill="#1a9bd7"/><circle cx="9" cy="7.3" r="1" fill="#1a9bd7"/><circle cx="12.5" cy="7.3" r="1" fill="#1a9bd7"/></svg>
      <span>Contact</span>
    </div>
  </nav>
</div>
</body>
</html>
```